Golden Pantry Spice

Distributor of seasonings and spices to the restaurant industry.

Industry/Entity Type

Restaurant

Contact Information for Business Card

Golden Pantry
Derek Hollings
TW Brandvik Distributor
316-487-9021
derek@goldpantryspicehub.com

No minimum order
Gluten & MSG free soup bases

```html
<!DOCTYPE html>
<html lang="en">
<head>
<meta charset="utf-8">
<title>Golden Pantry Spice – Business Card</title>
<link rel="stylesheet" href="https://fonts.googleapis.com/css2?family=Lato:wght@300;400;700&display=swap">
<style>
  :root {
    --backdrop: #d9d9d9;
    --card-navy: #172a45;
    --gold: #f4c27c;
    --gold-soft: #e9b872;
  }
  * { margin: 0; padding: 0; box-sizing: border-box; }
  html, body {
    width: 1200px;
    height: 1023px;
    overflow: hidden;
    background: var(--backdrop);
    font-family: "Lato", Arial, sans-serif;
  }
  .stage {
    width: 1200px;
    height: 1023px;
    display: flex;
    align-items: center;
    justify-content: center;
  }
  .business-card {
    position: relative;
    width: 900px;
    height: 514px;
    background: var(--card-navy);
    color: var(--gold);
  }
  .rule {
    position: absolute;
    background: var(--gold);
  }
  .rule--h { height: 1.5px; }
  .rule--v { width: 1.5px; }

  .rule--logo-top    { left: 70px;  top: 150px; width: 330px; }
  .rule--logo-bottom { left: 70px;  top: 395px; width: 330px; }
  .rule--divider     { left: 420px; top: 130px; height: 280px; }
  .rule--name-top    { left: 440px; top: 100px; width: 390px; }
  .rule--contact     { left: 440px; top: 262px; width: 390px; }
  .rule--offer       { left: 440px; top: 370px; width: 390px; }

  .brand {
    position: absolute;
    left: 70px;
    top: 215px;
    width: 330px;
    display: flex;
    align-items: center;
    gap: 14px;
  }
  .brand__dot {
    width: 18px;
    height: 18px;
    border-radius: 50%;
    background: var(--gold);
    flex: none;
  }
  .brand__name {
    font-weight: 300;
    font-size: 40px;
    line-height: 1;
    color: var(--gold);
    white-space: nowrap;
  }
  .brand__role {
    position: absolute;
    left: 70px;
    top: 340px;
    font-weight: 300;
    font-size: 22px;
    color: var(--gold-soft);
  }

  .contact {
    position: absolute;
    left: 445px;
    top: 130px;
  }
  .contact__name {
    font-weight: 700;
    font-size: 42px;
    line-height: 1.1;
    color: var(--gold);
  }
  .contact__line {
    font-weight: 300;
    font-size: 21px;
    line-height: 1.45;
    color: var(--gold-soft);
  }
  .contact__phone { margin-top: 12px; }

  .offer {
    position: absolute;
    left: 445px;
    top: 282px;
  }
  .offer__line {
    font-weight: 400;
    font-size: 22px;
    line-height: 1.5;
    color: var(--gold);
  }
</style>
</head>
<body>
<main class="stage">
  <section class="business-card" aria-label="Golden Pantry business card">
    <span class="rule rule--h rule--logo-top"></span>
    <span class="rule rule--h rule--logo-bottom"></span>
    <span class="rule rule--v rule--divider"></span>
    <span class="rule rule--h rule--name-top"></span>
    <span class="rule rule--h rule--contact"></span>
    <span class="rule rule--h rule--offer"></span>

    <div class="brand">
      <span class="brand__dot"></span>
      <span class="brand__name">Golden Pantry</span>
    </div>
    <p class="brand__role">TW Brandvik Distributor</p>

    <div class="contact">
      <h1 class="contact__name">Derek Hollings</h1>
      <p class="contact__line contact__phone">316-487-9021</p>
      <p class="contact__line">derek@goldpantryspicehub.com</p>
    </div>

    <div class="offer">
      <p class="offer__line">No minimum order</p>
      <p class="offer__line">Gluten &amp; MSG free soup bases</p>
    </div>
  </section>
</main>
</body>
</html>
```